COVID-19 Related Signage for Hotel

Need to create new COVID-19 related signage utilizing our brand assets. Please use screenshots for copy/direction. essentially duplicate the screenshots but with our logo/branding.

All brand assets have been uploaded and examples of signage content. Pictures are not necessary but you can add them if you want similar to the examples attached.

Sign requirements

sign 1. Text "Hand Sanitizer Station" can add graphic
sign 2. Text "Protect Yourself" duplicate copy in the attached pictures
sign 3. Text "Face Mask Required" can add graphic
sign 4. Text "Face Covering Do's and Don'ts with text from "Face-covering checklist.jpg" REMOVE BWR logo or website or 3 face mask graphics
sign 5. Text "Maintain 6 Foot Distance" This sign will be printed and placed on the ground for guests to know where to stand in queue. Would prefer a circular Design. sign 6. Text "Wet, Lather, Scrub, Rinse, Dry" similar to screenshots attached.

ALL signs should have same look and feel throughout utilizing our brand graphics, logo, colors, and guidelines.

Target Market(s)

Hotel Guests

Industry/Entity Type

Hotel

Font styles to use
Sans Serif

Requirements
Must have
• Cohesive, unified branding look and feel

Should not have
• any use of the word "COVID-19" or Coronavirus.

```html
<!DOCTYPE html>
<html lang="en">
<head>
<meta charset="utf-8">
<title>Face Covering Do's and Don'ts – Ridge Hollow Lodge</title>
<link rel="stylesheet" href="https://fonts.googleapis.com/css2?family=Oswald:wght@500;600;700&display=swap">
<style>
  :root {
    --backdrop: #5f5366;
    --teal: #17aab8;
    --orange: #f47b20;
    --orange-deep: #c85a0c;
    --white: #ffffff;
    --figure-tone: #1394a1;
  }
  * { box-sizing: border-box; margin: 0; padding: 0; }
  html, body { width: 1200px; height: 790px; overflow: hidden; }
  body {
    background: var(--backdrop);
    font-family: "Oswald", "Arial Narrow", sans-serif;
    position: relative;
  }
  .sign {
    position: absolute;
    background: var(--white);
    border-radius: 16px;
  }
  .sign__frame {
    position: absolute;
    inset: 8px;
    border: 6px solid var(--orange);
    border-radius: 12px;
    overflow: hidden;
  }
  .sign--portrait { left: 78px; top: 93px; width: 428px; height: 605px; }
  .sign--landscape { left: 554px; top: 183px; width: 603px; height: 425px; }

  .el { position: absolute; }

  .title {
    color: var(--white);
    font-weight: 600;
    text-transform: uppercase;
    white-space: nowrap;
  }
  .heading {
    color: var(--orange);
    font-weight: 700;
    text-transform: uppercase;
    line-height: 1;
    white-space: nowrap;
    text-shadow: 2px 2px 0 var(--orange-deep);
  }
  .rule { height: 1.5px; background: var(--orange); }
  .list { list-style: none; }
  .list li {
    position: absolute;
    left: 0;
    color: var(--teal);
    font-weight: 500;
    line-height: 21px;
    text-transform: uppercase;
    white-space: nowrap;
  }
  .list svg { position: absolute; left: 0; top: 1px; width: 19px; height: 19px; }

  .figure {
    position: absolute;
    background: linear-gradient(180deg, var(--figure-tone) 0%, var(--teal) 70%, var(--orange) 100%);
    border-radius: 50% 50% 6px 6px;
  }
  .brand {
    position: absolute;
    display: flex;
    align-items: center;
    justify-content: center;
    gap: 6px;
    font-weight: 500;
    font-size: 17px;
    line-height: 24px;
    text-transform: lowercase;
    white-space: nowrap;
  }
  .brand__dot { width: 10px; height: 10px; border-radius: 50%; }

  /* portrait */
  .sign--portrait .header { left: 0; top: 0; width: 100%; height: 155px; background: var(--teal); }
  .sign--portrait .title { left: 118px; top: 26px; font-size: 42px; line-height: 50px; letter-spacing: -0.8px; }
  .sign--portrait .figure { left: 22px; top: 13px; width: 90px; height: 142px; }
  .sign--portrait .heading { left: 0; width: 100%; text-align: center; font-size: 50px; }
  .sign--portrait .rule { left: 28px; width: 342px; }
  .sign--portrait .list { left: 28px; }
  .sign--portrait .list li { font-size: 17px; padding-left: 25px; }
  .sign--portrait .brand { left: 0; width: 100%; top: 515px; color: var(--orange); }
  .sign--portrait .brand__dot { background: var(--orange); }

  /* landscape */
  .sign--landscape .sidebar { left: 0; top: 0; width: 216px; height: 100%; background: var(--teal); }
  .sign--landscape .title { left: 12px; top: 18px; font-size: 28px; line-height: 33px; letter-spacing: -0.5px; }
  .sign--landscape .figure { left: 38px; top: 95px; width: 128px; height: 178px; }
  .sign--landscape .brand { left: 0; width: 216px; top: 325px; color: var(--white); }
  .sign--landscape .brand__dot { background: var(--white); }
  .sign--landscape .heading { left: 232px; font-size: 56px; }
  .sign--landscape .rule { left: 232px; width: 331px; }
  .sign--landscape .list { left: 206px; }
  .sign--landscape .list li { font-size: 18px; padding-left: 27px; }
</style>
</head>
<body>
  <svg width="0" height="0" style="position:absolute" aria-hidden="true">
    <defs>
      <symbol id="icon-tick" viewBox="0 0 20 20">
        <circle cx="10" cy="10" r="10" fill="#f47b20"/>
        <path d="M5.5 10.3l3 3 6-6.3" fill="none" stroke="#fff" stroke-width="2.4" stroke-linecap="round" stroke-linejoin="round"/>
      </symbol>
      <symbol id="icon-cross" viewBox="0 0 20 20">
        <circle cx="10" cy="10" r="10" fill="#f47b20"/>
        <path d="M6.5 6.5l7 7M13.5 6.5l-7 7" fill="none" stroke="#fff" stroke-width="2.4" stroke-linecap="round"/>
      </symbol>
    </defs>
  </svg>

  <!-- Portrait sign -->
  <section class="sign sign--portrait">
    <div class="sign__frame">
      <div class="el header"></div>
      <div class="figure" role="img" aria-label="Illustration of a person wearing a face mask"></div>
      <h1 class="el title">Face Covering<br>Do’s and Don’ts</h1>

      <h2 class="el heading" style="top:162px;">Do:</h2>
      <div class="el rule" style="top:213px;"></div>
      <ul class="el list" style="top:220px;">
        <li style="top:0"><svg><use href="#icon-tick"/></svg>Make sure you can breathe through it</li>
        <li style="top:27px"><svg><use href="#icon-tick"/></svg>Wear it whenever going out in public</li>
        <li style="top:54px"><svg><use href="#icon-tick"/></svg>Make sure it covers your nose and mouth</li>
        <li style="top:82px"><svg><use href="#icon-tick"/></svg>Wash after using</li>
      </ul>

      <h2 class="el heading" style="top:354px;">Don’t:</h2>
      <div class="el rule" style="top:407px;"></div>
      <ul class="el list" style="top:410px;">
        <li style="top:0"><svg><use href="#icon-cross"/></svg>Use if under two years old</li>
        <li style="top:33px"><svg><use href="#icon-cross"/></svg>Use surgical masks or other PPE intended<br>for healthcare workers</li>
      </ul>

      <div class="brand"><span class="brand__dot"></span>ridge hollow lodge</div>
    </div>
  </section>

  <!-- Landscape sign -->
  <section class="sign sign--landscape">
    <div class="sign__frame">
      <div class="el sidebar"></div>
      <h1 class="el title">Face Covering<br>Do’s and Don’ts</h1>
      <div class="figure" role="img" aria-label="Illustration of a person wearing a face mask"></div>
      <div class="brand"><span class="brand__dot"></span>ridge hollow lodge</div>

      <h2 class="el heading" style="top:17px;">Do:</h2>
      <div class="el rule" style="top:85px;"></div>
      <ul class="el list" style="top:92px;">
        <li style="top:0"><svg><use href="#icon-tick"/></svg>Make sure you can breathe through it</li>
        <li style="top:28px"><svg><use href="#icon-tick"/></svg>Wear it whenever going out in public</li>
        <li style="top:57px"><svg><use href="#icon-tick"/></svg>Make sure it covers your nose and mouth</li>
        <li style="top:86px"><svg><use href="#icon-tick"/></svg>Wash after using</li>
      </ul>

      <h2 class="el heading" style="top:227px;">Don’t:</h2>
      <div class="el rule" style="top:288px;"></div>
      <ul class="el list" style="top:292px;">
        <li style="top:0"><svg><use href="#icon-cross"/></svg>Use if under two years old</li>
        <li style="top:34px"><svg><use href="#icon-cross"/></svg>Use surgical masks or other PPE intended<br>for healthcare workers</li>
      </ul>
    </div>
  </section>
</body>
</html>
```